Home Care company needs letter head branding

Home care company needs a letter head which can be used for all documents the company's clients view. We provided in home care for the elderly. We would like to use our company colors (2785A7, 0A4057 and 34A74D) and should not be too large as we will be using it on more than just a letter head but all documents our clients sign / receive.
Target Market(s)
Professional business
Industry/Entity Type
Health Care
Requirements
Must have
- corporate brand colors

```html
<!DOCTYPE html>
<html lang="en">
<head>
<meta charset="utf-8">
<title>Elmstead Care — Letterhead</title>
<link rel="stylesheet" href="https://fonts.googleapis.com/css2?family=Lato:wght@400;700&display=swap">
<style>
  :root {
    --brand-teal: #2785A7;
    --brand-navy: #0A4057;
    --brand-green: #34A74D;
    --text-dark: #3a3f44;
    --backdrop: #e6e6e6;
    --paper: #ffffff;
    --canopy-blue: #d5e6ed;
    --canopy-green: #edf3dc;
  }
  html, body {
    margin: 0;
    padding: 0;
    width: 1200px;
    height: 866px;
    overflow: hidden;
    background: var(--backdrop);
    font-family: "Lato", Arial, sans-serif;
  }
  .letterhead {
    position: absolute;
    left: 347px;
    top: 62px;
    width: 535px;
    height: 749px;
    background: var(--paper);
    overflow: hidden;
  }
  .brand {
    position: absolute;
    left: 35px;
    top: 50px;
    display: flex;
    align-items: center;
    gap: 7px;
  }
  .brand-mark {
    width: 43px;
    height: 43px;
    border-radius: 50%;
    border: 2px solid var(--brand-teal);
    box-sizing: border-box;
  }
  .brand-name {
    font-family: "Lato", Arial, sans-serif;
    font-weight: 700;
    font-size: 23px;
    color: var(--brand-teal);
    letter-spacing: -0.2px;
  }
  .contact {
    position: absolute;
    left: 378px;
    top: 38px;
    font-size: 8.6px;
    line-height: 11.5px;
    color: var(--text-dark);
  }
  .contact-address {
    margin: 0 0 6px 0;
  }
  .contact-list {
    list-style: none;
    margin: 0;
    padding: 0;
  }
  .contact-list li {
    display: flex;
    align-items: center;
    gap: 4px;
    height: 13px;
  }
  .contact-icon {
    width: 9px;
    height: 9px;
    flex: none;
  }
  .canopy-art {
    position: absolute;
    left: 0;
    bottom: 0;
    width: 329px;
    height: 342px;
    border-radius: 0 62% 8% 0 / 0 55% 20% 0;
    background: radial-gradient(ellipse at 65% 45%, var(--canopy-green) 0%, var(--canopy-green) 45%, var(--canopy-blue) 100%);
    opacity: 0.85;
  }
</style>
</head>
<body>
  <main class="letterhead">
    <header class="brand">
      <span class="brand-mark" aria-hidden="true"></span>
      <span class="brand-name">Elmstead Care</span>
    </header>

    <address class="contact" style="font-style: normal;">
      <p class="contact-address">1820 Linden Park Ave, Suite B140<br>Rockville MD 20850</p>
      <ul class="contact-list">
        <li>
          <svg class="contact-icon" viewBox="0 0 10 10" aria-hidden="true">
            <circle cx="5" cy="5" r="5" fill="var(--brand-teal)"/>
            <path d="M3.3 2.6l1 1-.5.6c.3.7.8 1.2 1.5 1.5l.6-.5 1 1-.7.8C4.6 6.8 3 5.2 2.8 3.2z" fill="#fff"/>
          </svg>
          (301) 555-0142
        </li>
        <li>
          <svg class="contact-icon" viewBox="0 0 10 10" aria-hidden="true">
            <circle cx="5" cy="5" r="5" fill="var(--brand-teal)"/>
            <rect x="2.4" y="3.2" width="5.2" height="3.6" fill="none" stroke="#fff" stroke-width="0.8"/>
            <path d="M2.4 3.2L5 5.3l2.6-2.1" fill="none" stroke="#fff" stroke-width="0.8"/>
          </svg>
          info@elmsteadcare.com
        </li>
        <li>
          <svg class="contact-icon" viewBox="0 0 10 10" aria-hidden="true">
            <circle cx="5" cy="5" r="5" fill="var(--brand-teal)"/>
            <circle cx="5" cy="5" r="2.7" fill="none" stroke="#fff" stroke-width="0.7"/>
            <path d="M2.3 5h5.4M5 2.3c-1.2 1.5-1.2 3.9 0 5.4M5 2.3c1.2 1.5 1.2 3.9 0 5.4" fill="none" stroke="#fff" stroke-width="0.6"/>
          </svg>
          www.elmsteadcare.com
        </li>
      </ul>
    </address>

    <div class="canopy-art" role="img" aria-label="Faint illustration of a tree with pale blue branches and soft green leaves"></div>
  </main>
</body>
</html>
```